Business Card for Ferncliff Massage

I need a business card for my massage therapy & cannabis oil practice. I already have a logo,the "massage" got edited out of this file. I will send the original soon. I need these elements to be on the card:
web: FerncliffMassage.example
ph: 417/283-9061
email: Mirela.Dawkant@mailbox.example
Other slogans, statements to consider:
Science Geek, Massage Therapist, Neuromuscular Therapy, Cannabis Spa Treatments, Raindrop Therapy, Essential Oils
Target Market(s)
women between 20 & 65, people with enough $ to afford regular massage, people who recently had a motor vehicle accident, Halvora HMP insured
Industry/Entity Type
Massage Therapy
Contact Information for Business Card
I would like to see my bear logo featured; contact details, greens & blues preferred colors.

```html
<!DOCTYPE html>
<html lang="en">
<head>
<meta charset="utf-8">
<title>Ferncliff Massage – Business Card</title>
<link href="https://fonts.googleapis.com/css2?family=Open+Sans:wght@400;600;700&display=swap" rel="stylesheet">
<style>
  :root {
    --green: #2e8a3c;
    --green-dark: #1f6a2b;
    --green-light: #3a9a47;
    --ink: #222222;
    --paper: #ffffff;
    --paper-shade: #f1f1f1;
    --backdrop: #e6e3dd;
    --stone: #a59c97;
  }
  * { box-sizing: border-box; margin: 0; padding: 0; }
  html, body { width: 1200px; height: 800px; overflow: hidden; }
  body {
    background: var(--backdrop);
    font-family: "Open Sans", Arial, sans-serif;
    position: relative;
  }
  .card {
    position: absolute;
    left: 280px;
    width: 640px;
    height: 366px;
    box-shadow: 0 6px 18px rgba(0,0,0,0.18);
    overflow: hidden;
  }
  /* Front */
  .card-front {
    top: 24px;
    background: linear-gradient(135deg, var(--paper) 0%, var(--paper) 60%, var(--paper-shade) 100%);
  }
  .identity {
    position: absolute;
    left: 44px;
    top: 58px;
    padding-left: 16px;
    border-left: 7px solid var(--green);
  }
  .identity-name {
    font-size: 25px;
    color: var(--ink);
    font-weight: 400;
    line-height: 1.1;
  }
  .identity-name strong { font-weight: 700; }
  .identity-title {
    font-size: 16px;
    color: var(--green);
    line-height: 1.2;
  }
  .brand {
    position: absolute;
    right: 50px;
    top: 120px;
    display: flex;
    align-items: center;
    gap: 12px;
  }
  .brand-dot {
    width: 34px; height: 34px;
    border-radius: 50%;
    background: var(--stone);
  }
  .brand-name {
    font-size: 38px;
    font-weight: 400;
    color: var(--green);
    letter-spacing: 0.5px;
  }
  .contacts {
    position: absolute;
    left: 44px;
    bottom: 40px;
    list-style: none;
  }
  .contacts li {
    display: flex;
    align-items: center;
    gap: 14px;
    font-size: 17px;
    color: var(--ink);
    margin-top: 8px;
  }
  .contact-icon {
    width: 24px; height: 24px;
    border-radius: 5px;
    background: var(--green);
    display: flex; align-items: center; justify-content: center;
    flex-shrink: 0;
  }
  /* Back */
  .card-back {
    top: 410px;
    background: radial-gradient(ellipse at 70% 20%, var(--green-light) 0%, var(--green) 45%, var(--green-dark) 100%);
    color: var(--paper);
  }
  .services {
    position: absolute;
    left: 50px;
    bottom: 44px;
    list-style: none;
  }
  .services li {
    display: flex;
    align-items: center;
    gap: 8px;
    font-size: 18px;
    line-height: 1.5;
  }
  .brand-back {
    position: absolute;
    right: 54px;
    top: 110px;
    display: flex;
    align-items: center;
    gap: 12px;
  }
  .brand-back .brand-dot { background: rgba(255,255,255,0.85); }
  .brand-back .brand-name { color: var(--paper); font-size: 34px; }
</style>
</head>
<body>
  <section class="card card-front" aria-label="Business card front">
    <div class="identity">
      <p class="identity-name">Mirela <strong>Dawkant</strong></p>
      <p class="identity-title">Job Title</p>
    </div>

    <div class="brand">
      <span class="brand-dot"></span>
      <span class="brand-name">Ferncliff Massage</span>
    </div>

    <ul class="contacts">
      <li>
        <span class="contact-icon">
          <svg width="12" height="16" viewBox="0 0 12 16"><rect x="1" y="1" width="10" height="14" rx="2" fill="none" stroke="#fff" stroke-width="1.6"/><circle cx="6" cy="12" r="1" fill="#fff"/></svg>
        </span>
        417/283-9061
      </li>
      <li>
        <span class="contact-icon">
          <svg width="16" height="12" viewBox="0 0 16 12"><rect x="1" y="1" width="14" height="10" fill="none" stroke="#fff" stroke-width="1.5"/><path d="M1 1 L8 7 L15 1" fill="none" stroke="#fff" stroke-width="1.5"/></svg>
        </span>
        Mirela.Dawkant@mailbox.example
      </li>
      <li>
        <span class="contact-icon">
          <svg width="16" height="16" viewBox="0 0 16 16"><circle cx="8" cy="8" r="6.5" fill="none" stroke="#fff" stroke-width="1.3"/><ellipse cx="8" cy="8" rx="3" ry="6.5" fill="none" stroke="#fff" stroke-width="1.1"/><line x1="1.5" y1="8" x2="14.5" y2="8" stroke="#fff" stroke-width="1.1"/></svg>
        </span>
        FerncliffMassage.example
      </li>
    </ul>
  </section>

  <section class="card card-back" aria-label="Business card back">
    <div class="brand-back">
      <span class="brand-dot"></span>
      <span class="brand-name">Ferncliff Massage</span>
    </div>

    <ul class="services">
      <li><svg width="18" height="16" viewBox="0 0 18 16"><rect x="1" y="4" width="11" height="11" fill="none" stroke="#fff" stroke-width="1.4"/><path d="M3 9 L7 13 L17 1" fill="none" stroke="#fff" stroke-width="2.2"/></svg>Science Geek</li>
      <li><svg width="18" height="16" viewBox="0 0 18 16"><rect x="1" y="4" width="11" height="11" fill="none" stroke="#fff" stroke-width="1.4"/><path d="M3 9 L7 13 L17 1" fill="none" stroke="#fff" stroke-width="2.2"/></svg>Massage Therapist</li>
      <li><svg width="18" height="16" viewBox="0 0 18 16"><rect x="1" y="4" width="11" height="11" fill="none" stroke="#fff" stroke-width="1.4"/><path d="M3 9 L7 13 L17 1" fill="none" stroke="#fff" stroke-width="2.2"/></svg>Neuromuscular Therapy</li>
      <li><svg width="18" height="16" viewBox="0 0 18 16"><rect x="1" y="4" width="11" height="11" fill="none" stroke="#fff" stroke-width="1.4"/><path d="M3 9 L7 13 L17 1" fill="none" stroke="#fff" stroke-width="2.2"/></svg>Cannabis Spa Treatments</li>
      <li><svg width="18" height="16" viewBox="0 0 18 16"><rect x="1" y="4" width="11" height="11" fill="none" stroke="#fff" stroke-width="1.4"/><path d="M3 9 L7 13 L17 1" fill="none" stroke="#fff" stroke-width="2.2"/></svg>Raindrop Therapy</li>
      <li><svg width="18" height="16" viewBox="0 0 18 16"><rect x="1" y="4" width="11" height="11" fill="none" stroke="#fff" stroke-width="1.4"/><path d="M3 9 L7 13 L17 1" fill="none" stroke="#fff" stroke-width="2.2"/></svg>Essential Oils</li>
    </ul>
  </section>
</body>
</html>
```